Cobalt MesaLighting and Design Web Page

We are a Sales Agency that represents 40+ LED Lighting manufacturers primarily in new commercial, industrial and architectural construction projects. We also are active in the Re-Light and Retrofit Lighting market.
Our current web page can be found at www.cobaltmesalighting.example. Our local competitors are www.brightfieldlampsnw.example,. We would like a more dynamic website that will list our manufacturers we represent and links to their websites. Please offer suggestions to provide a more dynamic website using our new logo which is attached. Please use the color scheme from logo. The final design should communicate innovation and expertise in LED lighting.

Target Market(s)

Architects, Lighting designers, Electrical Engineers, Electrical Contractors, Electrical Distributors, Facility Engineers, Energy Engineers

Industry/Entity Type

Construction

Number of Pages Required

5+ page

Font styles to use
Other font styles liked:
• MS Reference Sans Serif, or close to our LOGO font.

Colors
f78f20
959595

Requirements
Must have
• Logo incorporated with matching background, clean professional look based on logo, links to our manufacturers web page
Nice to have
• LED Lighting project stock photos as examples
Should not have
• crowded pages with text

```html
<!DOCTYPE html>
<html lang="en">
<head>
<meta charset="utf-8">
<title>Cobalt Mesa Lighting — LED Lighting Experts</title>
<link href="https://fonts.googleapis.com/css2?family=Questrial&family=Open+Sans:wght@400;600&display=swap" rel="stylesheet">
<style>
  :root {
    --accent: #e2592a;
    --ink: #222222;
    --text: #444444;
    --muted: #8a8a8a;
    --band: #f1f1f1;
    --footer: #f2f2f2;
    --rule: #d6d6d6;
    --white: #ffffff;
  }
  * { box-sizing: border-box; margin: 0; padding: 0; }
  html, body { width: 1200px; height: 2715px; overflow: hidden; }
  body {
    position: relative;
    background: var(--white);
    font-family: "Open Sans", Arial, sans-serif;
    color: var(--text);
  }
  .abs { position: absolute; }

  /* Header */
  .site-header { position: absolute; left: 0; top: 0; width: 1200px; height: 136px; }
  .brand { position: absolute; left: 132px; top: 40px; display: flex; align-items: center; gap: 12px; }
  .brand-dot { width: 34px; height: 34px; border-radius: 50%; background: var(--accent); }
  .brand-name { font-family: "Questrial", Arial, sans-serif; font-size: 26px; color: var(--accent); }
  .phone { position: absolute; right: 133px; top: 34px; font-family: "Questrial", sans-serif; font-size: 21px; color: var(--ink); display: flex; align-items: center; gap: 8px; }
  .main-nav { position: absolute; right: 133px; top: 80px; display: flex; gap: 30px; font-size: 13px; color: var(--text); }
  .main-nav .current { color: var(--accent); }

  /* Hero */
  .hero { position: absolute; left: 0; top: 136px; width: 1200px; height: 479px;
    background: linear-gradient(100deg, #8a6a45 0%, #c9a77a 35%, #e6c79a 55%, #b88a5a 80%, #7c5a3a 100%); }
  .hero-title { position: absolute; left: 0; width: 1200px; top: 192px; text-align: center;
    font-family: "Questrial", sans-serif; font-size: 38px; color: var(--white); letter-spacing: 1px; }
  .quote-btn { position: absolute; left: 532px; top: 240px; width: 135px; height: 40px; background: var(--white);
    color: var(--accent); font-size: 15px; display: flex; align-items: center; justify-content: center; }
  .slide-arrow { position: absolute; top: 224px; width: 22px; height: 32px; background: rgba(60,60,60,.55); }
  .slide-arrow.prev { left: 0; } .slide-arrow.next { right: 0; }

  /* Welcome */
  .welcome { position: absolute; left: 132px; top: 680px; width: 936px; text-align: center; }
  .welcome h1 { font-family: "Questrial", sans-serif; font-weight: 400; font-size: 40px; color: var(--accent); }
  .welcome .lead { margin-top: 14px; font-size: 16px; line-height: 25px; color: var(--ink); }
  .welcome .detail { margin-top: 18px; font-size: 11.5px; line-height: 21px; color: var(--muted); text-align: justify; text-align-last: center; }
  .welcome .closing { margin-top: 16px; font-size: 19px; color: var(--accent); }

  /* Services grid */
  .service { position: absolute; width: 448px; text-align: center; }
  .service .photo { width: 448px; height: 239px; }
  .service h2 { margin-top: 6px; font-family: "Questrial", sans-serif; font-weight: 400; font-size: 23px; color: var(--accent); }

  /* Works */
  .works { position: absolute; left: 0; top: 1689px; width: 1200px; height: 297px; background: var(--band); }
  .works h2 { position: absolute; left: 0; width: 1200px; top: 42px; text-align: center;
    font-family: "Questrial", sans-serif; font-weight: 400; font-size: 23px; color: var(--ink); }
  .works-arrow { position: absolute; top: 45px; width: 24px; height: 24px; border: 1px solid #b9b9b9; background: var(--white); }
  .work { position: absolute; top: 105px; height: 192px; }

  /* Blog */
  .blog-title { position: absolute; left: 132px; top: 2068px; font-family: "Questrial", sans-serif; font-size: 24px; color: var(--accent); }
  .view-all { position: absolute; right: 133px; top: 2080px; font-size: 10px; color: var(--text); }
  .post { position: absolute; top: 2123px; width: 297px; }
  .post .photo { height: 161px; }
  .post h3 { margin-top: 16px; font-weight: 400; font-size: 14px; color: var(--ink); }
  .post p { margin-top: 8px; font-size: 10.5px; line-height: 15px; color: var(--muted); }
  .post .more { display: block; margin-top: 8px; font-size: 10px; color: var(--ink); }

  /* Footer */
  .site-footer { position: absolute; left: 0; top: 2474px; width: 1200px; height: 241px; background: var(--footer); }
  .contact-col { position: absolute; top: 40px; font-size: 12px; line-height: 18px; color: var(--text); }
  .contact-col h4 { font-weight: 400; font-size: 15px; color: var(--accent); margin-bottom: 4px; }
  .footer-rule { position: absolute; left: 132px; top: 127px; width: 936px; height: 1px; background: var(--rule); }
  .footer-nav { position: absolute; left: 132px; top: 161px; font-size: 11px; color: var(--text); }
  .footer-nav span.sep { margin: 0 9px; color: #999; }
  .copyright { position: absolute; left: 132px; top: 189px; font-size: 11px; color: var(--text); }
  .social { position: absolute; right: 133px; top: 174px; display: flex; gap: 6px; }
  .social span { width: 26px; height: 26px; border-radius: 50%; }
</style>
</head>
<body>

<header class="site-header">
  <div class="brand"><span class="brand-dot"></span><span class="brand-name">Cobalt Mesa Lighting</span></div>
  <div class="phone">
    <svg width="12" height="18" viewBox="0 0 12 18"><rect x="1" y="1" width="10" height="16" rx="2" fill="none" stroke="#222" stroke-width="2"/><rect x="4" y="13" width="4" height="1.5" fill="#222"/></svg>
    Phone : 555-014-0370
  </div>
  <nav class="main-nav">
    <span class="current">Home</span><span>About</span><span>Line Card</span><span>Services</span><span>Territory Map</span><span>Photo Gallery</span><span>Blog</span><span>Contact</span>
  </nav>
</header>

<section class="hero">
  <div class="abs" role="img" aria-label="Modern kitchen lit by warm recessed ceiling lights and glowing LED backsplash" style="inset:0"></div>
  <div class="slide-arrow prev"><svg width="22" height="32"><path d="M13 10l-6 6 6 6" stroke="#fff" stroke-width="1.5" fill="none"/></svg></div>
  <div class="slide-arrow next"><svg width="22" height="32"><path d="M9 10l6 6-6 6" stroke="#fff" stroke-width="1.5" fill="none"/></svg></div>
  <div class="hero-title">INTEGER CONVALLIS URNA</div>
  <div class="quote-btn">GET A QUOTE</div>
</section>

<section class="welcome">
  <h1>Welcome</h1>
  <p class="lead">Cobalt Mesa Lighting was established in 1996 and is the leading lighting and controls agency in the region servicing West Texas, New Mexico, and Mexico (Country).</p>
  <p class="detail">We are a team of experienced and talented individuals who share the same passion: “Exceed customer and manufacturer expectations by providing high-quality technical support and the best in class customer service”, experts in LED Lighting systems for architectural, commercial, industrial, institutional, and residential purposes as well as controls projects. We are here to support your needs in energy saving, sustainability, and green building initiatives such as the Verdant Building Standard (VBS) and the Campus Sustainability Index (CSI). With highly selective LED lighting varieties, we supersede the expectations of our customers and manufacturers with guaranteed value and unparalleled performance.</p>
  <p class="closing">We look forward in working with you!</p>
</section>

<div class="service" style="left:132px; top:1033px;">
  <div class="photo" role="img" aria-label="Bright living room with recessed cove ceiling lighting and chandelier" style="background:linear-gradient(160deg,#f4f1ec,#cfc7bb 60%,#8f8678);"></div>
  <h2>Design Assistance</h2>
</div>
<div class="service" style="left:619px; top:1033px;">
  <div class="photo" role="img" aria-label="Technician installing a recessed ceiling downlight" style="background:linear-gradient(120deg,#d9d6d3,#eeeeee 55%,#c9463a 90%);"></div>
  <h2>Training</h2>
</div>
<div class="service" style="left:132px; top:1337px;">
  <div class="photo" role="img" aria-label="Industrial steel truss roof fitted with high-bay lights" style="background:linear-gradient(170deg,#b9bcc2,#7d8189 55%,#4a4d55);"></div>
  <h2>Project Management</h2>
</div>
<div class="service" style="left:619px; top:1337px;">
  <div class="photo" role="img" aria-label="Highway overpass lit blue at night" style="background:linear-gradient(150deg,#0e1a33,#2d5fb0 50%,#0b1428);"></div>
  <h2>Energy Saving Projects</h2>
</div>

<section class="works">
  <div class="works-arrow" style="left:132px;"><svg width="22" height="22"><path d="M13 7l-4 4 4 4" stroke="#888" fill="none"/></svg></div>
  <div class="works-arrow" style="left:1044px;"><svg width="22" height="22"><path d="M9 7l4 4-4 4" stroke="#888" fill="none"/></svg></div>
  <h2>Our Works</h2>
  <div class="work" role="img" aria-label="White architectural light fixture against blue wall" style="left:0; width:232px; background:linear-gradient(180deg,#5a7fc4,#3f62a8);"></div>
  <div class="work" role="img" aria-label="Atrium with skylight and balconies" style="left:243px; width:231px; background:linear-gradient(180deg,#8fb6de,#d9d4c8 55%,#6f7a86);"></div>
  <div class="work" role="img" aria-label="Warmly lit shopping arcade at night" style="left:485px; width:232px; background:linear-gradient(180deg,#6b3a14,#e0a040 50%,#5a2e12);"></div>
  <div class="work" role="img" aria-label="Restaurant interior with pendant lighting" style="left:726px; width:231px; background:linear-gradient(180deg,#8a5a30,#c98a4e 50%,#3e2514);"></div>
  <div class="work" role="img" aria-label="Building facade washed in purple and blue LED light" style="left:968px; width:232px; background:linear-gradient(90deg,#2a3bd0,#c02fc8 50%,#3a2ab8);"></div>
</section>

<div class="blog-title">Blog</div>
<div class="view-all">VIEW ALL</div>

<article class="post" style="left:132px;">
  <div class="photo" role="img" aria-label="Living room with blue LED cove ceiling" style="background:linear-gradient(170deg,#f3f3f5,#b9bfca 55%,#5a4a3e);"></div>
  <h3>Nulla dignissim convallis volutpat</h3>
  <p>Donec eget rhoncus nulla. Suspendisse tincidunt commodo cursus. Duis finibus ante tortor sapien, vel commodo augue tempor eu...</p>
  <span class="more">More</span>
</article>
<article class="post" style="left:451px;">
  <div class="photo" role="img" aria-label="Ornate golden dome ceiling lit from below" style="background:radial-gradient(circle at 50% 55%,#f6d38a,#c07a28 50%,#6a3410);"></div>
  <h3>Donec at eros eu nulla porta scelerisque</h3>
  <p>Donec eget rhoncus nulla. Suspendisse tincidunt commodo cursus. Duis finibus ante tortor sapien, vel commodo augue tempor eu...</p>
  <span class="more">More</span>
</article>
<article class="post" style="left:769px;">
  <div class="photo" role="img" aria-label="Bathroom with warm wall sconces and glass shower" style="background:linear-gradient(160deg,#e8dccb,#a88c6c 55%,#4e3a28);"></div>
  <h3>Donec ullamcorper sodales purus</h3>
  <p>Donec eget rhoncus nulla. Suspendisse tincidunt commodo cursus. Duis finibus ante tortor sapien, vel commodo augue tempor eu...</p>
  <span class="more">More</span>
</article>

<footer class="site-footer">
  <div class="contact-col" style="left:132px; width:240px;"><h4>Cobalt Mesa Lighting</h4>4410 Aster Loop, Sunvale Texas, United States 79000</div>
  <div class="contact-col" style="left:396px;"><h4>Email for the US:</h4>sales@cobaltmesalighting.example</div>
  <div class="contact-col" style="left:628px;"><h4>Email for Latin America:</h4>ventas@cobaltmesalighting.example</div>
  <div class="contact-col" style="left:858px;"><h4>Email for Design Support:</h4>applications@cobaltmesalighting.example</div>
  <div class="footer-rule"></div>
  <nav class="footer-nav">Home<span class="sep">|</span>About<span class="sep">|</span>Line Card<span class="sep">|</span>Services<span class="sep">|</span>Territory Map<span class="sep">|</span>Photo Gallery<span class="sep">|</span>Blog<span class="sep">|</span>Contact</nav>
  <div class="copyright">Copyright © 2017 Cobalt Mesa Lighting. All rights reserved.</div>
  <div class="social">
    <span style="background:#3b5a99"></span><span style="background:#2aa3e0"></span><span style="background:#f08a24"></span>
  </div>
</footer>

</body>
</html>
```